Hearth Keepers Brochure - marketing an innovative home maintenance subscription program

We would like a brochure for this new service offering.
Hearth Keepers offers a subscription based home maintenance program that is quite unique. Everyone goes to the dentist for regular checkups and cleanings, or takes their car for oil changes, but too few pay that much attention to their largest asset - their home. So we fill that niche. We need a good brochure to promote the quarterly maintenance and our general contracting services.

Target Market(s)

Upper-Middle Class, SF Bay Area, Home Owner. Techies without know-how or time, single women, and elderly families or those with vacation homes.

Industry/Entity Type

Handyman and general contracting (residential construction and maintenance)

Font styles to use
Serif

Colors
0054AA
0677BA
7BADD7
CADEEF
E8F1F8

Requirements
Must have
• Basic contact info for www.HearthKeepers.example, some sort of hook, logo, etc.
Nice to have
• Something awesome!
Should not have
• Want classy, not cheap or flashy. Must have good balance for high-end homeowners in San Francisco Bay Area.

```html
<!DOCTYPE html>
<html lang="en">
<head>
<meta charset="utf-8">
<title>Hearth Keepers Brochure</title>
<link rel="stylesheet" href="https://fonts.googleapis.com/css2?family=Nunito:wght@400;600;700&family=Lato:wght@400;700&display=swap">
<style>
  :root{
    --backdrop:#7fcfb8;
    --paper:#f2f2f0;
    --leaf-green:#5f9c38;
    --sun-yellow:#e9ad16;
    --ember-orange:#e05b1e;
    --ink:#2a2a2a;
    --ink-soft:#3b3b3b;
    --navy:#243a7a;
    --slate:#3d4250;
    --band:rgba(240,240,240,.88);
  }
  *{box-sizing:border-box;margin:0;padding:0}
  html,body{width:1200px;height:800px;overflow:hidden}
  body{background:var(--backdrop);font-family:"Lato",sans-serif;color:var(--ink-soft)}
  .brochure{position:absolute;left:120px;top:20px;width:960px;height:760px;display:flex;box-shadow:0 8px 24px rgba(0,0,0,.18)}
  .panel{position:relative;width:320px;height:760px;background:var(--paper);overflow:hidden}
  .photo{position:absolute}
  .body-copy{font-size:11px;line-height:25px;text-align:justify;color:var(--ink-soft)}
  .nowrap{white-space:nowrap}

  /* panel one */
  .intro-heading{position:absolute;left:24px;top:40px;width:280px;font-family:"Nunito",sans-serif;font-weight:400;font-size:20px;line-height:34px;color:var(--leaf-green)}
  .intro-copy{position:absolute;left:24px;top:150px;width:276px;font-size:10.5px;line-height:23px}
  .intro-copy .inset{float:right;width:172px;height:138px;margin:4px 0 4px 8px;background:linear-gradient(135deg,#e8e8e8 0%,#bdb7ae 55%,#8c7c6b 100%)}
  .crawlspace{left:0;top:432px;width:320px;height:328px;background:linear-gradient(180deg,#c9a75a 0%,#a07a3c 45%,#6b5a44 75%,#9c9488 100%)}
  .phone-band{position:absolute;left:0;top:682px;width:320px;height:52px;background:var(--band);display:flex;align-items:center;justify-content:center;gap:8px;font-family:"Nunito",sans-serif;font-size:29px;font-weight:600;color:var(--slate)}

  /* panel two */
  .process-copy{position:absolute;left:30px;top:34px;width:264px;line-height:25.5px}
  .house{position:absolute;left:0;top:0}
  .hook{position:absolute;left:0;top:310px;width:320px;text-align:center;font-family:"Nunito",sans-serif}
  .hook .lead{display:block;font-size:19px;color:var(--navy);font-weight:600}
  .hook .punch{display:block;font-size:33px;color:var(--ink);font-weight:600;line-height:42px}
  .tile{position:absolute;width:142px;height:148px}
  .tile.washer{left:26px;top:392px;border-radius:48px 0 48px 0;background:linear-gradient(135deg,#f4f4f4,#cfcfcf)}
  .tile.filter{left:176px;top:392px;border-radius:0 48px 0 48px;background:linear-gradient(135deg,#e9d9c6,#8aa9c8 60%,#dcdcdc)}
  .tile.vent{left:26px;top:548px;border-radius:0 48px 0 48px;background:linear-gradient(135deg,#e3e8ee,#f7f7f7 50%,#c3ccd8)}
  .tile.repair{left:176px;top:598px;border-radius:48px 0 48px 0;background:linear-gradient(135deg,#e7d6c4,#8b6b55 55%,#d9d9d9)}

  /* panel three */
  .services-title{position:absolute;left:26px;top:32px;font-family:"Nunito",sans-serif;font-weight:600;font-size:21px;color:var(--ember-orange);white-space:nowrap}
  .services-copy{position:absolute;left:26px;top:74px;width:268px}
  .services-copy p+p{margin-top:24px}
  .roofer{left:0;top:500px;width:320px;height:260px;background:linear-gradient(160deg,#6e7f3e 0%,#3e4a5c 45%,#9a9690 80%);z-index:0}
  .service-list{position:absolute;left:0;top:360px;width:320px;height:184px;background:var(--ember-orange);border-radius:0 60px 0 36px;list-style:none;padding:12px 0 0 30px;z-index:1}
  .service-list li{display:flex;align-items:center;gap:12px;font-size:11px;line-height:26px;color:#fff}
  .brand-band{position:absolute;left:0;top:690px;width:320px;height:56px;background:var(--band);display:flex;align-items:center;justify-content:center;gap:8px;z-index:2}
  .brand-mark{width:18px;height:18px;background:var(--navy)}
  .brand-name{font-family:"Nunito",sans-serif;font-weight:700;font-size:24px;color:var(--navy);letter-spacing:.5px}
</style>
</head>
<body>
<main class="brochure">

  <section class="panel panel-intro">
    <h2 class="intro-heading">We keep one of your largest assets in great condition, and let you enjoy your weekends.</h2>
    <div class="intro-copy body-copy">
      <div class="inset" role="img" aria-label="Photo of an electrician fitting a wall outlet"></div>
      This system has been perfected for over 20 years. Here’s how it works. During an initial intake inspection we inventory all major systems and appliances, and generate a punch list of any deferred maintenance. Using this information we can respond more quickly when things break, and we create a roadmap to address any problems.
    </div>
    <div class="photo crawlspace" role="img" aria-label="Photo of an insulated crawlspace with ductwork"></div>
    <div class="phone-band">
      <svg width="26" height="26" viewBox="0 0 24 24" aria-hidden="true"><path d="M6.6 2.8l2.6 3.6-1.6 2.2c1 2.4 3.4 4.8 5.8 5.8l2.2-1.6 3.6 2.6-1.4 3.4C11 18.6 5.4 13 4.2 4.2z" fill="none" stroke="#3d4250" stroke-width="1.4"/></svg>
      <span>415-555-0142</span>
    </div>
  </section>

  <section class="panel panel-process">
    <p class="process-copy body-copy"><strong>Then, using seasonal checklists,</strong> a two-person team inspects and repairs over 250 items annually. Our GC Division manages any larger repairs or “special projects.” Financial advisors recommend budgeting <span class="nowrap">1-4%</span> of the value of a home for annual maintenance. Hearth Keepers is the most cost-efficient way to maintain your home.</p>
    <svg class="house" width="320" height="760" viewBox="0 0 320 760" aria-hidden="true">
      <path d="M0 305 L160 180 L210 219 L210 200 Q210 195 215 195 L268 195 Q273 195 273 200 L273 268 L320 305 L320 760 L0 760 Z" fill="#e9ad16"/>
      <path d="M168 556 Q212 552 220 600 Q176 604 168 556 Z" fill="#5f9c38"/>
      <path d="M128 740 Q130 700 170 694 Q168 736 128 740 Z" fill="#e05b1e"/>
    </svg>
    <h1 class="hook"><span class="lead">Let us Maintain your Home, so</span><span class="punch">you don’t Have to.</span></h1>
    <div class="tile washer" role="img" aria-label="Photo of a front-loading washing machine"></div>
    <div class="tile filter" role="img" aria-label="Photo of hands servicing a water filter"></div>
    <div class="tile vent" role="img" aria-label="Photo of a gloved hand cleaning an air vent"></div>
    <div class="tile repair" role="img" aria-label="Photo of a technician repairing an appliance"></div>
  </section>

  <section class="panel panel-services">
    <h2 class="services-title">General Contracting Services</h2>
    <div class="services-copy body-copy">
      <p>Hearth Keepers residential services fall into two categories. For homeowners and property managers wishing to keep up with maintenance and have routine inspections and services provided; we offer the Hearth Keepers Program.</p>
      <p>For homes that have fallen in disrepair or just need tuning up beyond the Hearth Keepers seasonal maintenance, we offer General Contracting Services assisting our clients in bringing their home back to good health.</p>
    </div>
    <div class="photo roofer" role="img" aria-label="Photo of a roofer using a nail gun on shingles"></div>
    <ul class="service-list">
      <li><svg width="16" height="8" viewBox="0 0 16 8" aria-hidden="true"><path d="M0 8 L8 0 L16 8 Z" fill="#fff"/></svg>Kitchen and bath remodels</li>
      <li><svg width="16" height="8" viewBox="0 0 16 8" aria-hidden="true"><path d="M0 8 L8 0 L16 8 Z" fill="#fff"/></svg>New landscape installations and decks</li>
      <li><svg width="16" height="8" viewBox="0 0 16 8" aria-hidden="true"><path d="M0 8 L8 0 L16 8 Z" fill="#fff"/></svg>New roofs, siding, doors and windows</li>
      <li><svg width="16" height="8" viewBox="0 0 16 8" aria-hidden="true"><path d="M0 8 L8 0 L16 8 Z" fill="#fff"/></svg>Site drainage</li>
      <li><svg width="16" height="8" viewBox="0 0 16 8" aria-hidden="true"><path d="M0 8 L8 0 L16 8 Z" fill="#fff"/></svg>Indoor air quality improvements</li>
      <li><svg width="16" height="8" viewBox="0 0 16 8" aria-hidden="true"><path d="M0 8 L8 0 L16 8 Z" fill="#fff"/></svg>Home comfort and HVAC upgrades</li>
    </ul>
    <div class="brand-band">
      <span class="brand-mark" aria-hidden="true"></span>
      <span class="brand-name">HEARTH KEEPERS</span>
    </div>
  </section>

</main>
</body>
</html>
```